Business Card Design Project For Moving Company

Hello,

We need the business card to be 2 sided and we were thinking to use the logo on the front of the card (see file 1 attached) and the text "logo" (see file 2 attached) in the back of the card. We're looking for a powerful design that will help us build our brand, as our company is new.
We are a full service moving company (no storage) located in San Diego, CA, USA. The design should communicate to our potential customers that we have the highest level of service, customer satisfaction is our number one goal, our team is professional and efficient.

Thank you,

Dorn
Updates

Project Deadline Extended
Reason: We would like to have more time to provide feedback for the designs already submitted. Thank you, Dorn

Industry/Entity Type

Moving Company

Requirements
Must have
• Front of the card must have the following text and logo:
Haulbright, Inc
Residential And Commercial
Local And Long Distance
Address: 7312 Quillmont Rd, #146,
San Diego, CA, 92784
P: 855-372-LIFT (5438)
F: 858-529-4407
info@haul-bright.com
www.haul-bright.com

Back of the card must have the following text and text "logo" (file 2 attached):

The best compliment we can ever receive is a referral from our clients.

```html
<!DOCTYPE html>
<html lang="en">
<head>
<meta charset="utf-8">
<title>Haulbright Business Card</title>
<link href="https://fonts.googleapis.com/css2?family=Arimo:wght@400;700&family=Oswald:wght@500;700&display=swap" rel="stylesheet">
<style>
  :root {
    --page: #ffffff;
    --denim-dark: #1c1c1c;
    --denim-mid: #3a3a3a;
    --brand-red: #e0261f;
    --ink: #1e1e1e;
    --card-edge: #e2e2e2;
    --white: #ffffff;
  }
  * { margin: 0; padding: 0; box-sizing: border-box; }
  html, body { width: 960px; height: 1200px; overflow: hidden; background: var(--page); }
  .canvas { position: relative; width: 960px; height: 1200px; font-family: "Arimo", Arial, sans-serif; color: var(--ink); }

  .card { position: absolute; left: 95px; width: 789px; height: 453px; }

  /* Card back */
  .card-back { top: 93px; overflow: hidden; }
  .card-back .texture {
    position: absolute; inset: 0;
    background: radial-gradient(ellipse at 50% 45%, var(--denim-mid) 0%, var(--denim-dark) 85%);
  }
  .emblem {
    position: absolute; left: 50%; top: 213px; transform: translate(-50%, -50%);
    width: 234px; height: 216px; border-radius: 50%;
    background: var(--white); border: 7px solid #151515;
    display: flex; align-items: center; justify-content: center;
  }
  .emblem-name {
    font-family: "Oswald", "Arial Narrow", sans-serif; font-weight: 700;
    font-size: 34px; letter-spacing: 1px; color: var(--brand-red); text-transform: uppercase;
  }

  /* Card front */
  .card-front { top: 618px; background: var(--white); border: 1px solid var(--card-edge); }
  .wordmark {
    position: absolute; right: 26px; top: 22px;
    font-family: "Oswald", "Arial Narrow", sans-serif; font-weight: 700;
    font-size: 33px; line-height: 1; color: var(--brand-red); text-transform: uppercase; letter-spacing: -0.5px;
  }
  .name-band { position: absolute; left: 0; top: 201px; width: 508px; height: 52px; }
  .name-band svg { position: absolute; inset: 0; }
  .name-band .holder {
    position: relative; padding-left: 27px; line-height: 52px;
    font-size: 25px; color: var(--white);
  }
  .services {
    position: absolute; left: 26px; top: 320px;
    font-family: "Oswald", "Arial Narrow", sans-serif; font-weight: 700;
    font-size: 17px; letter-spacing: 0.1px; color: var(--ink); text-transform: uppercase;
  }
  .contact { position: absolute; top: 393px; font-size: 19.5px; line-height: 26px; color: #2a2a2a; }
  .contact.address { left: 26px; }
  .contact.phones { left: 272px; }
  .contact.online { left: 547px; }
  .dot { position: absolute; top: 416px; width: 9px; height: 9px; border-radius: 50%; background: var(--brand-red); }
  .dot.first { left: 247px; }
  .dot.second { left: 521px; }
</style>
</head>
<body>
<main class="canvas">

  <section class="card card-back" aria-label="Card back">
    <div class="texture" role="img" aria-label="Dark charcoal denim fabric texture"></div>
    <div class="emblem"><span class="emblem-name">Haulbright</span></div>
  </section>

  <section class="card card-front" aria-label="Card front">
    <div class="wordmark">Haulbright</div>

    <div class="name-band">
      <svg width="508" height="52" viewBox="0 0 508 52" aria-hidden="true">
        <polygon points="0,0 508,0 478,52 0,52" fill="var(--brand-red)"/>
      </svg>
      <p class="holder">Ellis Warren / 91-9744 52 6120</p>
    </div>

    <p class="services">Residential and Commercial / Local and Long Distance</p>

    <p class="contact address">7312 Quillmont Rd, #146,<br>San Diego, CA, 92784</p>
    <span class="dot first"></span>
    <p class="contact phones">P: 855-372-LIFT (5438)<br>F: 858-529-4407</p>
    <span class="dot second"></span>
    <p class="contact online">info@haul-bright.com<br>www.haul-bright.com</p>
  </section>

</main>
</body>
</html>
```